Email signature design - law firm

We are a small boutique law firm which is located near the beach in Manly, Australia.

We have just recently developed a new logo and are looking to redesign our letterhead, business cards and email signatures.

This brief is for our email signatures. This is an email signature to appear at the bottom of our Outlook emails so we would like it to be text that we are able to edit as the wording in our email signature often required amendments.

I have attached a word document which had our new logo, and our previous email signature which all the information/wording that needs to be included.

We would like multiple designs with a modern, simplistic yet striking look.

Thanks.

font - raleway or montserrat

Need extra days to review

• Must have the exact wording which appears in the email signature in the word document attached to brief.
• Must be able to edit the text as it is for an Outlook email signature which wording will change from time to time.

```html
<!DOCTYPE html>
<html lang="en">
<head>
<meta charset="utf-8">
<title>Harlow &amp; Partners – Stationery Set</title>
<link rel="stylesheet" href="https://fonts.googleapis.com/css2?family=Arimo:wght@400;700&family=Montserrat:wght@500;600&family=Noto+Sans:wght@400&display=swap">
<style>
  :root {
    --navy: #34418f;
    --blue: #6f86c9;
    --gold: #c4aa6c;
    --ink: #111111;
    --muted: #6b6b6b;
    --frame: #8a8a8a;
    --paper: #ffffff;
  }
  * { margin: 0; padding: 0; box-sizing: border-box; }
  html, body { width: 1200px; height: 848px; overflow: hidden; background: var(--paper); }
  .sheet { position: relative; width: 1200px; height: 848px; font-family: "Arimo", Arial, sans-serif; color: var(--ink); }

  .section-title { position: absolute; font-family: "Noto Sans", Verdana, sans-serif; font-weight: 400; font-size: 24px; line-height: 1; color: var(--ink); }
  .section-title.letterhead-title { left: 76px; top: 19px; }
  .section-title.card-title { left: 778px; top: 182px; width: 200px; text-align: center; }
  .section-title.signature-title { left: 778px; top: 475px; width: 200px; text-align: center; }

  .frame { position: absolute; border: 1px solid var(--frame); background: var(--paper); }
  .letterhead { left: 55px; top: 67px; width: 534px; height: 755px; }
  .business-card { left: 691px; top: 230px; width: 362px; height: 227px; }

  /* Name mark */
  .brand { position: absolute; display: flex; flex-direction: column; align-items: center; }
  .brand-row { display: flex; align-items: center; gap: 5px; }
  .brand-dot { border-radius: 50%; background: var(--navy); flex: none; }
  .brand-name { font-family: "Montserrat", Arial, sans-serif; font-weight: 600; color: var(--navy); letter-spacing: 0.06em; white-space: nowrap; }
  .brand-tag { font-family: "Montserrat", Arial, sans-serif; font-weight: 500; color: var(--muted); letter-spacing: 0.55em; white-space: nowrap; }

  .letterhead .brand { left: 20px; top: 44px; width: 92px; }
  .letterhead .brand-dot { width: 9px; height: 9px; }
  .letterhead .brand-name { font-size: 7.4px; }
  .letterhead .brand-tag { font-size: 4px; margin-top: 4px; }

  .business-card .brand { left: 20px; top: 60px; width: 112px; }
  .business-card .brand-dot { width: 11px; height: 11px; }
  .business-card .brand-name { font-size: 8.6px; }
  .business-card .brand-tag { font-size: 5px; margin-top: 5px; }

  .signature .brand { left: 666px; top: 640px; width: 136px; }
  .signature .brand-dot { width: 13px; height: 13px; }
  .signature .brand-name { font-size: 10.6px; }
  .signature .brand-tag { font-size: 6px; margin-top: 6px; }

  .divider { position: absolute; width: 1px; background: #9a9a9a; }
  .letterhead .divider { left: 117px; top: 10px; height: 69px; }
  .signature .divider { left: 819px; top: 592px; height: 90px; }

  /* Contact block */
  .contact { position: absolute; }
  .contact-name { font-weight: 700; white-space: nowrap; }
  .contact-line { display: flex; align-items: center; white-space: nowrap; }
  .icon { flex: none; fill: var(--navy); }
  .fax { margin-left: 1.4em; }

  .letterhead .contact { left: 125px; top: 17px; font-size: 9.6px; line-height: 13.3px; }
  .letterhead .icon { width: 7px; height: 7px; margin-right: 2px; }

  .business-card .contact { left: 10px; top: 151px; font-size: 11.6px; line-height: 17.3px; }
  .business-card .icon { width: 10px; height: 10px; margin-right: 3px; }

  .signature .contact { left: 807px; top: 599px; font-size: 14px; line-height: 19.2px; }
  .signature .contact { left: 807px; }
  .signature .contact-name { font-size: 14.2px; margin-bottom: 1px; }
  .signature .contact { padding-left: 0; }
  .signature .contact { left: 807px; }
  .signature .contact-block { position: absolute; left: 808px; top: 598px; font-size: 14px; line-height: 19.4px; }
  .signature .contact-block .icon { width: 10px; height: 10px; margin-right: 3px; }
</style>
</head>
<body>
<svg width="0" height="0" style="position:absolute" aria-hidden="true">
  <defs>
    <symbol id="icon-phone" viewBox="0 0 24 24"><path d="M6.6 10.8a15.1 15.1 0 0 0 6.6 6.6l2.2-2.2c.3-.3.7-.4 1-.2 1.1.4 2.3.6 3.6.6.6 0 1 .4 1 1V20c0 .6-.4 1-1 1A17 17 0 0 1 3 4c0-.6.4-1 1-1h3.5c.6 0 1 .4 1 1 0 1.3.2 2.5.6 3.6.1.3 0 .7-.2 1z"/></symbol>
    <symbol id="icon-pin" viewBox="0 0 24 24"><path d="M12 2a7 7 0 0 0-7 7c0 5.2 7 13 7 13s7-7.8 7-13a7 7 0 0 0-7-7zm0 9.5A2.5 2.5 0 1 1 12 6.5a2.5 2.5 0 0 1 0 5z"/></symbol>
    <symbol id="icon-web" viewBox="0 0 24 24"><path d="M12 2a10 10 0 1 0 0 20 10 10 0 0 0 0-20zm6.9 6h-2.9a15.7 15.7 0 0 0-1.4-3.6A8 8 0 0 1 18.9 8zM12 4c.8 1.2 1.5 2.5 1.9 4h-3.8c.4-1.5 1.1-2.8 1.9-4zM4.3 14a8 8 0 0 1 0-4h3.4a16.5 16.5 0 0 0 0 4zm.8 2h2.9c.3 1.3.8 2.5 1.4 3.6A8 8 0 0 1 5.1 16zM8 8H5.1a8 8 0 0 1 4.3-3.6C8.8 5.5 8.3 6.7 8 8zm4 12c-.8-1.2-1.5-2.5-1.9-4h3.8c-.4 1.5-1.1 2.8-1.9 4zm2.3-6H9.7a14.7 14.7 0 0 1 0-4h4.6a14.7 14.7 0 0 1 0 4zm.3 5.6c.6-1.1 1.1-2.3 1.4-3.6h2.9a8 8 0 0 1-4.3 3.6zm1.7-5.6a16.5 16.5 0 0 0 0-4h3.4a8 8 0 0 1 0 4z"/></symbol>
  </defs>
</svg>

<main class="sheet">
  <h2 class="section-title letterhead-title">Letterhead</h2>

  <section class="frame letterhead" aria-label="Letterhead">
    <div class="brand">
      <div class="brand-row"><span class="brand-dot"></span><span class="brand-name">Harlow &amp; Partners</span></div>
      <span class="brand-tag">LAWYERS</span>
    </div>
    <span class="divider"></span>
    <div class="contact">
      <div class="contact-name">Harlow &amp; Partners</div>
      <div class="contact-line"><svg class="icon"><use href="#icon-phone"/></svg>(02) 9400 1180<span class="fax">Fax : (02) 9400 1190</span></div>
      <div class="contact-line"><svg class="icon"><use href="#icon-pin"/></svg>Suite 4, 12 Corso Lane, BAYVIEW, NSW 2104</div>
      <div class="contact-line"><svg class="icon"><use href="#icon-web"/></svg>www.harlowandpartners.com.au</div>
    </div>
  </section>

  <h2 class="section-title card-title">Business Card</h2>

  <section class="frame business-card" aria-label="Business card">
    <div class="brand">
      <div class="brand-row"><span class="brand-dot"></span><span class="brand-name">Harlow &amp; Partners</span></div>
      <span class="brand-tag">LAWYERS</span>
    </div>
    <div class="contact">
      <div class="contact-line"><svg class="icon"><use href="#icon-phone"/></svg>(02) 9400 1180<span class="fax">Fax : (02) 9400 1190</span></div>
      <div class="contact-line"><svg class="icon"><use href="#icon-pin"/></svg>Suite 4, 12 Corso Lane, BAYVIEW, NSW 2104</div>
      <div class="contact-line"><svg class="icon"><use href="#icon-web"/></svg>www.harlowandpartners.com.au</div>
    </div>
  </section>

  <h2 class="section-title signature-title">Signature</h2>

  <section class="signature" aria-label="Email signature">
    <div class="brand">
      <div class="brand-row"><span class="brand-dot"></span><span class="brand-name">Harlow &amp; Partners</span></div>
      <span class="brand-tag">LAWYERS</span>
    </div>
    <span class="divider"></span>
    <div class="contact-block">
      <div class="contact-name" style="margin-left:20px">Harlow &amp; Partners</div>
      <div class="contact-line" style="margin-left:17px"><svg class="icon"><use href="#icon-phone"/></svg>(02) 9400 1180<span class="fax">Fax : (02) 9400 1190</span></div>
      <div class="contact-line" style="margin-left:17px"><svg class="icon"><use href="#icon-pin"/></svg>Suite 4, 12 Corso Lane, BAYVIEW, NSW 2104</div>
      <div class="contact-line" style="margin-left:17px"><svg class="icon"><use href="#icon-web"/></svg>www.harlowandpartners.com.au</div>
    </div>
  </section>
</main>
</body>
</html>
```